Re-design existing website and add products for sale.

Our current website is very basic and cluttered. (emberfernwellness.com.au)We want a modern looking website that is easy to navigate. We also want to start selling essential oils and crystal products, so there needs to be a separate page for this. Also needs to be easily edited as we need to change the monthly oracle card with the description. Would like calming colours as we are all about natural healing. Alongside the services listed there should be a button to book now which asks for their name, email, phone number ect. and adds it to the cart.

• Logo is still being designed, please leave a space for the logo which will basically be a lotus flower within a mandala.

```html
<!DOCTYPE html>
<html lang="en">
<head>
<meta charset="utf-8">
<title>Ember Fern Wellness</title>
<link href="https://fonts.googleapis.com/css2?family=Courgette&family=Lato:wght@400;700&display=swap" rel="stylesheet">
<style>
:root{
  --purple:#9c6fae;
  --purple-deep:#7d4f93;
  --lavender:#efe8f7;
  --pink:#e3a7bc;
  --pink-soft:#f2cfdc;
  --mauve:#c49bbd;
  --text:#3f3a45;
  --muted:#6d6873;
  --line:#e2dde6;
  --white:#ffffff;
  --heading:#b58dc2;
}
*{box-sizing:border-box;margin:0;padding:0}
html,body{width:1200px;height:4478px;overflow:hidden}
body{font-family:'Lato',sans-serif;color:var(--text);background:var(--white);position:relative}
.script{font-family:'Courgette',cursive}
section,header,footer,.topbar{position:absolute;left:0;width:1200px}
.abs{position:absolute}

/* top bar */
.topbar{top:0;height:42px;background:linear-gradient(90deg,#c8a4cf,#b88fc4)}
.topbar ul{list-style:none;display:flex;gap:46px;position:absolute;right:50px;top:12px;font-size:13px;color:var(--white);letter-spacing:.5px}
.topbar li{display:flex;align-items:center;gap:8px}

/* header */
.site-header{top:42px;height:101px;background:var(--white)}
.brand{position:absolute;left:78px;top:16px;width:200px;text-align:center;font-family:'Courgette',cursive;font-size:28px;line-height:34px;color:var(--purple-deep)}
.main-nav{position:absolute;right:80px;top:38px;display:flex;gap:28px;font-size:14px;color:var(--text);letter-spacing:.3px}
.main-nav .active{color:var(--purple);border-bottom:2px solid var(--purple);padding-bottom:28px}

/* hero */
.hero{top:143px;height:558px;background:linear-gradient(90deg,#a678b3 0%,#b48bc4 45%,#9c6aac 100%)}
.hero-art{position:absolute;left:560px;top:0;width:640px;height:558px;background:radial-gradient(ellipse at 52% 70%,#fbf6ff 0%,#e6d3ef 22%,rgba(180,139,196,0) 55%)}
.hero h1{position:absolute;left:78px;top:178px;font-family:'Courgette',cursive;font-weight:400;font-size:46px;line-height:70px;color:var(--white)}

/* welcome */
.welcome{top:701px;height:657px;background:var(--white)}
.section-title{font-family:'Courgette',cursive;font-weight:400;color:var(--heading);font-size:36px;line-height:48px}
.welcome .section-title{position:absolute;left:80px;top:118px}
.welcome .copy{position:absolute;left:80px;top:290px;width:420px;font-size:15px;line-height:26px;color:var(--muted)}
.welcome .copy p+p{margin-top:14px}
.btn-pill{display:inline-block;width:210px;height:52px;border-radius:26px;background:linear-gradient(90deg,#f0c3d3,#d79bb6);color:var(--white);font-family:'Courgette',cursive;font-size:19px;line-height:52px;text-align:center;box-shadow:0 4px 10px rgba(200,140,170,.35)}
.welcome .btn-pill{position:absolute;left:78px;top:478px}
.blob{position:absolute;background:var(--pink-soft);border-radius:60px;transform:rotate(-35deg)}
.photo{position:absolute;border-radius:6px;box-shadow:0 6px 18px rgba(0,0,0,.12);border:5px solid var(--white)}

/* services */
.services{top:1358px;height:648px;background:linear-gradient(180deg,#ece3f6,#f3eef9)}
.services .section-title{position:absolute;left:0;width:1200px;text-align:center;top:52px;color:#c9a9d6;font-size:34px}
.services-figure{position:absolute;left:300px;top:130px;width:600px;height:518px;background:radial-gradient(ellipse at 50% 55%,#f7dbe8 0%,#ecc2d8 30%,rgba(236,227,246,0) 68%)}
.svc{position:absolute;display:flex;align-items:center;gap:22px;font-size:15px;line-height:21px;color:var(--text)}
.svc.left{right:calc(1200px - 320px);flex-direction:row;text-align:right}
.svc.right{left:880px;text-align:left}
.svc .icon{width:75px;height:75px;border-radius:50%;background:var(--mauve);display:flex;align-items:center;justify-content:center;flex-shrink:0}

/* products */
.products{top:2006px;height:770px;background:#fafafa}
.products .section-title{position:absolute;left:0;width:1200px;text-align:center;top:86px;font-size:34px}
.tabs{position:absolute;left:0;width:1200px;top:162px;display:flex;justify-content:center;gap:46px;font-size:16px;color:var(--text);letter-spacing:.5px}
.tabs .active{color:var(--muted);border-bottom:2px solid var(--pink);padding-bottom:12px}
.card{position:absolute;top:251px;width:322px;height:452px;background:var(--white);border:1px solid var(--line)}
.badge{position:absolute;left:18px;top:22px;width:134px;height:42px;border:1.5px solid var(--pink);color:var(--pink);font-size:14px;line-height:40px;text-align:center;letter-spacing:.5px}
.product-art{position:absolute;left:71px;top:110px;width:180px;height:150px;border-radius:8px}
.card h3{position:absolute;left:0;width:322px;top:318px;text-align:center;font-weight:400;font-size:15px;color:var(--text);letter-spacing:.5px}
.price{position:absolute;left:18px;top:368px;width:134px;height:46px;border:1px solid var(--line);text-align:center;line-height:44px;font-size:16px}
.buy{position:absolute;left:164px;top:368px;width:138px;height:46px;background:var(--pink);color:var(--text);text-align:center;line-height:46px;font-size:15px;font-weight:700}

/* oracle */
.oracle{top:2776px;height:487px;background:linear-gradient(90deg,#c59bbd 0%,#d5aec6 55%,#e4c0cd 100%)}
.oracle-scene{position:absolute;left:520px;top:0;width:420px;height:487px;background:radial-gradient(ellipse at 50% 40%,rgba(255,240,235,.45),rgba(255,240,235,0) 65%)}
.oracle .section-title{position:absolute;left:80px;top:128px;color:var(--white);font-size:34px}
.oracle .copy{position:absolute;left:80px;top:200px;width:560px;font-size:14px;line-height:23px;color:var(--white)}
.oracle .copy p+p{margin-top:16px}
.oracle-cards{position:absolute;left:756px;top:76px;width:440px;height:346px;background:linear-gradient(135deg,#3a2a7a,#5b4fb0 50%,#2f7fb8);border-radius:10px;transform:rotate(-3deg)}

/* about */
.about{top:3263px;height:617px;background:var(--white)}
.about-art{position:absolute;left:92px;top:80px;width:510px;height:500px;border-radius:50%;background:radial-gradient(circle,#f4c9e2 0%,#dcb4e2 45%,rgba(255,255,255,0) 72%)}
.about .section-title{position:absolute;left:657px;top:118px;width:380px;font-size:34px}
.about .rule{position:absolute;left:657px;top:252px;width:470px;height:1px;background:var(--line)}
.about .copy{position:absolute;left:657px;top:270px;width:470px;font-size:15px;line-height:25px;color:var(--muted)}
.about .copy p+p{margin-top:14px}
.about .btn-pill{position:absolute;left:657px;top:424px}

/* footer */
.site-footer{top:3880px;height:598px;background:linear-gradient(180deg,#d3b0cf 0%,#c7a1c6 40%,#e0b6c9 100%)}
.wave{position:absolute;left:0;top:-30px;width:1200px;height:170px}
.footer-brand{position:absolute;left:0;width:1200px;top:80px;text-align:center;font-family:'Courgette',cursive;font-size:28px;line-height:36px;color:var(--white)}
.newsletter-title{position:absolute;left:0;width:1200px;top:190px;text-align:center;font-size:20px;font-weight:700;color:var(--white)}
.subscribe{position:absolute;left:352px;top:240px;width:496px;height:54px;border-radius:27px;background:var(--white);box-shadow:0 0 0 6px rgba(255,255,255,.35)}
.subscribe span.ph{position:absolute;left:30px;top:18px;font-size:13px;color:#9a95a0}
.subscribe .go{position:absolute;right:10px;top:8px;width:140px;height:38px;border-radius:19px;background:linear-gradient(90deg,#c98fb6,#b77fae);color:var(--white);font-family:'Courgette',cursive;font-size:17px;text-align:center;line-height:38px}
.contact{position:absolute;top:400px;width:300px;text-align:center;color:var(--white);font-size:13px}
.contact svg{display:block;margin:0 auto 14px}
.footer-rule{position:absolute;left:80px;top:517px;width:1040px;height:1px;background:rgba(255,255,255,.45)}
.copyright{position:absolute;left:0;width:1200px;top:552px;text-align:center;color:var(--white);font-size:13px}
</style>
</head>
<body>

<div class="topbar">
  <ul>
    <li>BOOK NOW</li>
    <li><svg width="18" height="18" viewBox="0 0 18 18" fill="#fff"><circle cx="9" cy="5" r="4"/><path d="M1 18c0-5 3.5-7 8-7s8 2 8 7z"/></svg>MY ACCOUNT</li>
    <li><svg width="20" height="18" viewBox="0 0 20 18" fill="none" stroke="#fff" stroke-width="1.8"><path d="M1 2h3l2.5 10h10l2-7H6"/><circle cx="8" cy="16" r="1.3" fill="#fff"/><circle cx="15" cy="16" r="1.3" fill="#fff"/></svg>MY CART</li>
  </ul>
</div>

<header class="site-header">
  <div class="brand">Ember Fern<br>Wellness</div>
  <nav class="main-nav">
    <span class="active">HOME</span><span>ABOUT</span><span>SERVICES</span><span>ESSENTIAL OILS</span><span>CRYSTAL PRODUCTS</span><span>CONTACT</span>
  </nav>
</header>

<section class="hero">
  <div class="hero-art" role="img" aria-label="Glowing white lotus flower with sparkling light rising above it"></div>
  <h1>Find Your True Self<br>and Bring<br>Balance to Your Life</h1>
</section>

<section class="welcome">
  <h2 class="section-title">Welcome to Ember Fern<br>Wellness</h2>
  <div class="copy">
    <p>Are you struggling through life, feeling stuck, not feeling yourself, or simply feeling drained? Need to find a way to relax and rejuvenate, a way to free up your energy to work on that which better serves you in this lifetime?</p>
    <p>Working together with you, I can help you achieve this. Whether through spiritual healing sessions using Reiki.</p>
  </div>
  <span class="btn-pill">Know More</span>
  <div class="blob" style="left:560px;top:150px;width:120px;height:60px"></div>
  <div class="blob" style="left:960px;top:470px;width:140px;height:60px"></div>
  <div class="blob" style="left:780px;top:540px;width:90px;height:40px;opacity:.6"></div>
  <div class="photo" role="img" aria-label="Meditating figure with glowing chakra points" style="left:633px;top:80px;width:188px;height:218px;background:linear-gradient(160deg,#f5eef8,#d9c6e6)"></div>
  <div class="photo" role="img" aria-label="Woman with open arms in a sunlit field" style="left:839px;top:98px;width:188px;height:218px;background:linear-gradient(180deg,#8fb7d6,#d9c48a 70%,#a7935c)"></div>
  <div class="photo" role="img" aria-label="Woman relaxing with eyes closed" style="left:633px;top:320px;width:188px;height:218px;background:linear-gradient(160deg,#e8cbbd,#c69a86)"></div>
  <div class="photo" role="img" aria-label="Hands giving a Reiki healing treatment" style="left:839px;top:340px;width:188px;height:218px;background:linear-gradient(160deg,#d7a27a,#7a5a44)"></div>
</section>

<section class="services">
  <h2 class="section-title">Services We Provide</h2>
  <div class="services-figure" role="img" aria-label="Woman meditating cross-legged in front of a soft pink lotus"></div>

  <div class="svc left" style="top:142px"><span>Oracle Card<br>Readings</span><span class="icon"><svg width="32" height="32" viewBox="0 0 32 32" fill="none" stroke="#fff" stroke-width="2"><rect x="8" y="4" width="16" height="24" rx="2"/><path d="M12 10h8M12 16h8"/></svg></span></div>
  <div class="svc left" style="top:216px"><span>Distant Healing</span><span class="icon"><svg width="32" height="32" viewBox="0 0 32 32" fill="none" stroke="#fff" stroke-width="2"><path d="M16 4c5 6 8 10 8 15a8 8 0 0 1-16 0c0-5 3-9 8-15z"/></svg></span></div>
  <div class="svc left" style="top:312px"><span>Reiki &amp; Seichim<br>Workshops</span><span class="icon"><svg width="32" height="32" viewBox="0 0 32 32" fill="none" stroke="#fff" stroke-width="2"><circle cx="16" cy="16" r="10"/><circle cx="16" cy="16" r="4"/></svg></span></div>
  <div class="svc left" style="top:408px"><span>Crystals &amp; Hand<br>Made Jewellery</span><span class="icon"><svg width="32" height="32" viewBox="0 0 32 32" fill="none" stroke="#fff" stroke-width="2"><path d="M10 4h12l6 8-12 16L4 12z"/><path d="M4 12h24"/></svg></span></div>
  <div class="svc left" style="top:503px"><span>Essential Oil Roll<br>On Blends</span><span class="icon"><svg width="32" height="32" viewBox="0 0 32 32" fill="none" stroke="#fff" stroke-width="2"><rect x="11" y="10" width="10" height="18" rx="2"/><path d="M13 4h6v6h-6z"/></svg></span></div>

  <div class="svc right" style="top:120px"><span class="icon"><svg width="32" height="32" viewBox="0 0 32 32" fill="none" stroke="#fff" stroke-width="2"><circle cx="16" cy="16" r="11"/><circle cx="16" cy="16" r="5"/></svg></span><span>Reiki &amp; Seichim<br>Healings</span></div>
  <div class="svc right" style="top:216px"><span class="icon"><svg width="32" height="32" viewBox="0 0 32 32" fill="none" stroke="#fff" stroke-width="2"><path d="M18 3 8 18h8l-2 11 10-15h-8z"/></svg></span><span>Energy Healing</span></div>
  <div class="svc right" style="top:312px"><span class="icon"><svg width="32" height="32" viewBox="0 0 32 32" fill="none" stroke="#fff" stroke-width="2"><circle cx="16" cy="16" r="4"/><path d="M16 3v6M16 23v6M3 16h6M23 16h6M7 7l4 4M21 21l4 4M25 7l-4 4M11 21l-4 4"/></svg></span><span>Chakra<br>Balancing</span></div>
  <div class="svc right" style="top:408px"><span class="icon"><svg width="32" height="32" viewBox="0 0 32 32" fill="none" stroke="#fff" stroke-width="2"><circle cx="16" cy="16" r="11"/><path d="M9 9l14 14M23 9 9 23"/></svg></span><span>Energy<br>Balancing</span></div>
  <div class="svc right" style="top:503px"><span class="icon"><svg width="32" height="32" viewBox="0 0 32 32" fill="none" stroke="#fff" stroke-width="2"><path d="M16 5a11 11 0 1 0 11 11"/><path d="M27 6v6h-6"/></svg></span><span>Past Life<br>Clearing</span></div>
</section>

<section class="products">
  <h2 class="section-title">Our Products</h2>
  <div class="tabs"><span class="active">ALL</span><span>ESSENTIAL OILS</span><span>CRYSTAL PRODUCTS</span></div>

  <article class="card" style="left:78px">
    <span class="badge">NEW</span>
    <div class="product-art" role="img" aria-label="Blue crystal pendant with silver cap" style="background:radial-gradient(ellipse,#7fc8e8 0%,#e6f3f9 60%,#fff 75%)"></div>
    <h3>LOREM IPSUM IS DUMMY</h3>
    <span class="price">$649</span><span class="buy">BUY NOW</span>
  </article>
  <article class="card" style="left:439px">
    <span class="badge">NEW</span>
    <div class="product-art" role="img" aria-label="Amethyst pyramid energy generator with crystal points" style="background:radial-gradient(ellipse,#b7a0d8 0%,#ece6f4 60%,#fff 75%)"></div>
    <h3>LOREM IPSUM IS DUMMY</h3>
    <span class="price">$649</span><span class="buy">BUY NOW</span>
  </article>
  <article class="card" style="left:800px">
    <span class="badge">FEATURED</span>
    <div class="product-art" role="img" aria-label="Amber essential oil bottle" style="background:radial-gradient(ellipse,#8a4e1e 0%,#d9b89c 40%,#fff 72%)"></div>
    <h3>LOREM IPSUM IS DUMMY</h3>
    <span class="price">$649</span><span class="buy">BUY NOW</span>
  </article>
</section>

<section class="oracle">
  <div class="oracle-scene" role="img" aria-label="Faded figure with outstretched arms at sunset"></div>
  <h2 class="section-title">Monthly Oracle Card</h2>
  <div class="copy">
    <p>Lorem ipsum is simply dummy text of the printing and typesetting trade. Lorem ipsum has been the standard filler text ever since early print shops arranged loose type to make a simple sample book for layout.</p>
    <p>It has carried on through many changes, moving into digital typesetting and remaining much the same. It grew popular again with sheets of sample passages and later with desktop layout software that included it.</p>
  </div>
  <div class="oracle-cards" role="img" aria-label="Two oracle cards showing a winged glowing heart and a starry sky"></div>
</section>

<section class="about">
  <div class="about-art" role="img" aria-label="Pink and purple lotus mandala illustration within a circle"></div>
  <h2 class="section-title">About Ember Fern Wellness</h2>
  <div class="rule"></div>
  <div class="copy">
    <p>My love of all things spiritual and holistic started as a young girl and deepened when I first studied Reiki 19 years ago in 2000.</p>
    <p>After suffering with a hereditary medical problem from early childhood, I set about finding a solution in conjunction with modern medicine.</p>
  </div>
  <span class="btn-pill">Know More</span>
</section>

<footer class="site-footer">
  <svg class="wave" viewBox="0 0 1200 170" preserveAspectRatio="none">
    <path d="M0 30 C200 110 380 130 600 70 C820 10 1000 30 1200 60 V0 H0z" fill="#ffffff"/>
    <path d="M0 60 C250 140 420 120 640 90 C860 60 1000 80 1200 110" fill="none" stroke="rgba(255,255,255,.45)" stroke-width="3"/>
  </svg>
  <div class="footer-brand">Ember Fern<br>Wellness</div>
  <div class="newsletter-title">Subscribe to Our Newsletter</div>
  <div class="subscribe"><span class="ph">Enter your email</span><span class="go">Subscribe</span></div>

  <div class="contact" style="left:83px">
    <svg width="40" height="40" viewBox="0 0 40 40" fill="none" stroke="#fff" stroke-width="2"><path d="M10 5l6 7-4 4c2 5 6 9 11 11l4-4 7 6-4 6C17 34 6 23 5 10z"/></svg>
    0400 123 456
  </div>
  <div class="contact" style="left:450px">
    <svg width="40" height="40" viewBox="0 0 40 40" fill="none" stroke="#fff" stroke-width="2"><path d="M20 37s-11-12-11-21a11 11 0 0 1 22 0c0 9-11 21-11 21z"/><circle cx="20" cy="16" r="4"/></svg>
    12 Willow Lane Fernbrook, SA 5000
  </div>
  <div class="contact" style="left:805px">
    <svg width="40" height="40" viewBox="0 0 40 40" fill="none" stroke="#fff" stroke-width="2"><rect x="5" y="9" width="30" height="22"/><path d="M5 9l15 12 15-12"/></svg>
    hello@emberfernwellness.com.au
  </div>
  <div class="footer-rule"></div>
  <div class="copyright">©Ember Fern Wellness 2019 - All Rights Reserved.</div>
</footer>

</body>
</html>
```